Meadowlark Learning Growth Partners (MLGP)

This is a professional business card. Logo and picture are a must on the front of the card. I am an educational consultant. I have been consulting for the past three years for a company. I am now opening my own company. My goal for my consulting company is to eventually consult all over America.

Target Market(s)

Educators, schools, professionals

Industry/Entity Type

Consulting

Contact Information for Business Card

Picture/logo on front, simple modern design

Font styles to use
Serif

Colors
85abd2
0355a3
3176b5
cedeed

Requirements
Must have
• picture, logo,
• Odessa Pruitt, Ed.S
• address 5073 Cormorant ridge Dr. Nashville, TN 37940
• Cell:616-555-0148
• Office: 629-555-0172
• www.Mlgpedu.example
• pruittodessa@mailbox.example

```html
<!DOCTYPE html>
<html lang="en">
<head>
<meta charset="utf-8">
<title>Meadowlark Learning Growth Partners – Business Card</title>
<link rel="stylesheet" href="https://fonts.googleapis.com/css2?family=Lexend:wght@700&family=Arimo:wght@400&display=swap">
<style>
  :root {
    --navy: #0f3d83;
    --paper: #f6f5f0;
    --tint: #e9eff1;
    --rule: #c7daf0;
    --backdrop: #e4e4e2;
  }
  * { margin: 0; padding: 0; box-sizing: border-box; }
  html, body { width: 1200px; height: 1200px; overflow: hidden; }
  body { background: var(--backdrop); position: relative; }

  .card {
    position: absolute;
    left: 180px;
    width: 840px;
    height: 480px;
    background: var(--paper);
    overflow: hidden;
    box-shadow: 0 2px 8px rgba(0,0,0,0.12);
  }
  .card-front { top: 73px; }
  .card-back { top: 647px; }

  .card-tint { position: absolute; inset: 0; width: 840px; height: 480px; }

  .brand-mark {
    position: absolute;
    display: flex;
    align-items: center;
    gap: 16px;
    font-family: "Lexend", sans-serif;
    font-weight: 700;
    color: var(--navy);
  }
  .brand-mark .dot {
    background: var(--navy);
    border-radius: 50%;
    flex: none;
  }
  .card-front .brand-mark { left: 60px; top: 200px; font-size: 60px; letter-spacing: 4px; }
  .card-front .brand-mark .dot { width: 56px; height: 56px; }

  .divider-v {
    position: absolute;
    width: 2px;
    background: var(--navy);
  }
  .card-front .divider-v { left: 458px; top: 160px; height: 160px; }

  .company-name {
    position: absolute;
    left: 485px;
    top: 158px;
    font-family: "Lexend", sans-serif;
    font-weight: 700;
    font-size: 33px;
    line-height: 44px;
    color: var(--navy);
  }

  .card-back .brand-mark { left: 640px; top: 70px; font-size: 44px; letter-spacing: 3px; gap: 12px; }
  .card-back .brand-mark .dot { width: 40px; height: 40px; }

  .person {
    position: absolute;
    left: 22px;
    top: 186px;
    font-family: "Arimo", sans-serif;
    font-size: 25px;
    line-height: 32px;
    color: var(--navy);
  }
  .rule-h {
    position: absolute;
    left: 22px;
    top: 291px;
    width: 794px;
    height: 2px;
    background: var(--rule);
  }
  .card-back .divider-v { left: 418px; top: 327px; height: 120px; background: var(--rule); }

  .contact {
    position: absolute;
    font-family: "Arimo", sans-serif;
    color: var(--navy);
    font-style: normal;
  }
  .contact-address { left: 22px; top: 330px; font-size: 25px; line-height: 32px; }
  .contact-online { left: 483px; top: 412px; font-size: 23px; line-height: 32px; }
</style>
</head>
<body>

<section class="card card-front">
  <svg class="card-tint" viewBox="0 0 840 480" aria-hidden="true">
    <polygon points="840,8 430,250 810,480 840,480" fill="var(--tint)"/>
  </svg>
  <div class="brand-mark"><span class="dot"></span><span>MLGP</span></div>
  <div class="divider-v"></div>
  <h1 class="company-name">Meadowlark<br>Learning<br>Growth<br>Partners</h1>
</section>

<section class="card card-back">
  <svg class="card-tint" viewBox="0 0 840 480" aria-hidden="true">
    <polygon points="0,0 450,243 0,480" fill="var(--tint)"/>
  </svg>
  <div class="brand-mark"><span class="dot"></span><span>MLGP</span></div>
  <p class="person">Odessa Pruitt,<br>Education Specialist</p>
  <div class="rule-h"></div>
  <address class="contact contact-address">
    5073 Cormorant ridge Dr.<br>
    Nashville, TN 37940<br>
    Cell:616-555-0148<br>
    Office: 629-555-0172
  </address>
  <div class="divider-v"></div>
  <address class="contact contact-online">
    www.Mlgpedu.example<br>
    pruittodessa@mailbox.example
  </address>
</section>

</body>
</html>
```